Musician looking for catchy Web Design for promotion

My name is Brenna Colfer. I'm an Irish musician who plays the tin whistle and the flute. I'm also the leader of a traditional Irish music and dance ensemble called Wander the Hillside (www.wanderthehillside-example.com) and for the past 30 years, I've toured the world performing thousands of concerts. I run an annual cruise (www.brennacolfervoyage-example.com) that I would like a link to, and I'm also I'm organizing tours to Ireland that I would like a page set up for. I'm looking for a website to promote my tours and my music.
Updates

Hello Graphic Designers, I am only looking for the design of the home page to make my decision. Thank you. Brenna

Target Market(s)

Music fans of Irlsh and World Music

Industry/Entity Type

Entertainment Industry

Number of Pages Required

5+ page

Requirements
Must have
• I'm looking for a catchy design that shows a photo of me. I would like a few links....
• BIO
• TOURDATES
• BRENNA COLFER CRUISE
• MUSICAL TOUR OF IRELAND
• CONTACT
• VIDEO
• GALLERY
• CONTACT
• MAILING LIST
• STORE
Nice to have
• we'll see!

```html
<!DOCTYPE html>
<html lang="en">
<head>
<meta charset="utf-8">
<title>Brenna Colfer – Irish Musician</title>
<link href="https://fonts.googleapis.com/css2?family=Merriweather:ital,wght@0,400;0,700;1,400&family=Open+Sans:wght@400;600;700&display=swap" rel="stylesheet">
<style>
:root{
  --parchment:#eadcbd;
  --parchment-dark:#d6c39c;
  --page:#d8c7a2;
  --brown:#4e2f16;
  --brown-mid:#6d4624;
  --gold:#c9a45c;
  --ink:#3a2a1a;
  --text:#5b4e42;
  --panel:#fbf8f1;
  --footer:#1b1712;
  --footer-deep:#110e0b;
  --white:#ffffff;
}
*{box-sizing:border-box;margin:0;padding:0}
html,body{width:1200px;height:2236px;overflow:hidden}
body{position:relative;background:var(--page);font-family:'Open Sans',sans-serif;color:var(--text)}
.abs{position:absolute}

/* header */
.site-header{position:absolute;left:0;top:0;width:1200px;height:140px;background:linear-gradient(180deg,var(--parchment),var(--parchment-dark))}
.brand{left:150px;top:22px;display:flex;align-items:center;gap:14px}
.brand-mark{width:54px;height:54px;border-radius:50%;background:var(--brown)}
.brand-name{font-family:'Merriweather',serif;font-weight:700;color:var(--brown);font-size:18px;line-height:24px;letter-spacing:1px}
.contact-bar{left:780px;top:34px;display:flex;gap:40px}
.contact-item{display:flex;align-items:center;gap:10px;font-size:12px;color:var(--ink);line-height:16px}
.contact-item svg{width:30px;height:30px}
.contact-item b{display:block;font-size:11px;color:var(--brown-mid)}

/* nav */
.main-nav{position:absolute;left:0;top:140px;width:1200px;height:38px;background:linear-gradient(180deg,var(--brown-mid),var(--brown));border-top:2px solid var(--gold);border-bottom:2px solid var(--gold)}
.main-nav ul{list-style:none;display:flex;justify-content:space-between;width:900px;margin:0 auto;height:100%;align-items:center}
.main-nav li{font-size:12px;font-weight:700;color:var(--white);letter-spacing:.5px}

/* hero */
.hero{left:150px;top:192px;width:900px;height:400px;border:6px solid var(--white);box-shadow:0 2px 6px rgba(0,0,0,.25)}
.hero-photo{position:absolute;inset:0;background:linear-gradient(100deg,#8a7a6a 0%,#a59783 30%,#9fb6c2 55%,#6f8aa0 75%,#58714a 100%)}
.hero-text{left:560px;top:46px;width:310px;font-family:'Merriweather',serif;color:var(--white);font-size:22px;line-height:32px;text-align:center;text-shadow:0 1px 3px rgba(0,0,0,.5)}
.instrument{width:92px;height:92px;border-radius:50%;background:var(--brown);border:3px solid var(--gold);color:var(--white);font-family:'Merriweather',serif;font-size:13px;font-weight:700;display:flex;align-items:center;justify-content:center;text-align:center}
.slide-arrow{width:30px;height:30px;border-radius:50%;background:var(--brown);top:170px;display:flex;align-items:center;justify-content:center}
.slide-dots{left:0;top:598px;width:1200px;display:flex;justify-content:center;gap:8px}
.slide-dots span{width:9px;height:9px;border-radius:50%;background:var(--gold)}
.slide-dots span:first-child{background:var(--brown)}

/* panel */
.content-panel{left:150px;top:618px;width:900px;height:1342px;background:var(--panel)}
.section-title{font-family:'Merriweather',serif;font-weight:700;color:var(--ink);font-size:26px}
.title-center{left:0;width:900px;display:flex;align-items:center;justify-content:center;gap:18px}
.title-center::before,.title-center::after{content:"";width:250px;height:1px;background:var(--gold)}
.about-title{left:20px;top:14px;padding-bottom:8px;border-bottom:2px solid var(--gold)}
.about-text{left:20px;top:70px;width:540px;font-size:12.5px;line-height:20px}
.btn{display:inline-block;background:var(--brown);color:var(--white);font-size:11px;font-weight:700;padding:7px 14px;letter-spacing:.5px}
.video{left:580px;top:0px;width:300px;height:204px;background:#231b16;border:4px solid var(--white);box-shadow:0 1px 4px rgba(0,0,0,.3)}
.video-frame{position:absolute;left:0;top:0;width:292px;height:170px;background:linear-gradient(120deg,#3a2a22,#6a4a38 60%,#2c211b)}
.video-play{position:absolute;left:126px;top:65px;width:40px;height:40px;border-radius:50%;background:rgba(255,255,255,.85)}
.video-bar{position:absolute;left:10px;bottom:12px;width:272px;height:4px;background:#5a4a40}
.video-bar i{display:block;width:80px;height:4px;background:#c0392b}

.tour-card{top:312px;width:270px}
.tour-img{position:relative;height:170px;border:4px solid var(--white);box-shadow:0 1px 4px rgba(0,0,0,.3)}
.date-badge{position:absolute;right:8px;bottom:8px;color:var(--white);font-size:11px;font-weight:700;background:rgba(78,47,22,.85);padding:3px 6px}
.tour-card h3{font-family:'Merriweather',serif;font-size:15px;color:var(--ink);margin:14px 0 6px}
.tour-card p{font-size:12px;line-height:18px;margin-bottom:12px}

.gallery{left:20px;top:752px;width:860px;height:212px;display:grid;grid-template-columns:230px repeat(4,1fr);grid-template-rows:1fr 1fr;gap:8px}
.gallery div{background:linear-gradient(135deg,#3a2c22,#6b5242)}
.gallery .feature{grid-row:1/3;position:relative;background:linear-gradient(135deg,#4a3a30,#8a7060)}
.feature span{position:absolute;left:0;right:0;bottom:0;background:rgba(0,0,0,.6);color:var(--white);font-size:11px;padding:5px 8px}

.quote{top:1074px;width:410px;font-family:'Merriweather',serif;font-style:italic;font-size:12.5px;line-height:21px;color:var(--text)}
.quote cite{display:block;margin-top:10px;font-style:normal;font-size:12px;color:var(--gold);font-weight:700}
.quote cite span{color:var(--ink);font-weight:400}

/* footer */
.site-footer{position:absolute;left:0;top:1960px;width:1200px;height:240px;background:var(--footer);color:#cfc6b8}
.site-footer h4{font-size:14px;color:var(--white);margin-bottom:14px;font-weight:700}
.foot-col{top:30px}
.foot-col ul{list-style:none;font-size:12px;line-height:22px}
.field{width:180px;height:24px;background:var(--white);margin-bottom:8px}
.field.tall{height:48px}
.social li{display:flex;align-items:center;gap:10px;margin-bottom:6px}
.social li i{width:18px;height:18px;background:#6b5a48;display:block}
.foot-brand{left:860px;top:70px;display:flex;align-items:center;gap:12px}
.foot-brand .brand-mark{background:var(--gold);width:46px;height:46px}
.foot-brand .brand-name{color:var(--white);font-size:15px;line-height:21px}
.copyright{position:absolute;left:0;top:2200px;width:1200px;height:36px;background:var(--footer-deep);color:#8a8075;font-size:11px;display:flex;align-items:center;justify-content:center}
</style>
</head>
<body>

<header class="site-header">
  <div class="abs brand">
    <span class="brand-mark"></span>
    <div class="brand-name">BRENNA COLFER'S<br>MUSICAL TOUR OF IRELAND</div>
  </div>
  <div class="abs contact-bar">
    <div class="contact-item">
      <svg viewBox="0 0 30 30"><circle cx="15" cy="15" r="15" fill="#4e2f16"/><path d="M10 8l3 0 1 4-2 1.5c1 2 2.5 3.5 4.5 4.5l1.5-2 4 1v3c0 1-1 2-2 2C13 22 8 17 8 10c0-1 1-2 2-2z" fill="#fff"/></svg>
      <div><b>Call Us</b>123-456-7890</div>
    </div>
    <div class="contact-item">
      <svg viewBox="0 0 30 30"><circle cx="15" cy="15" r="15" fill="#4e2f16"/><rect x="8" y="10" width="14" height="10" fill="#fff"/><path d="M8 10l7 6 7-6" stroke="#4e2f16" stroke-width="1.5" fill="none"/></svg>
      <div><b>Email Us</b>info@brennacolfer-example.com</div>
    </div>
  </div>
</header>

<nav class="main-nav">
  <ul>
    <li>HOME</li><li>MEET THE STAFF</li><li>TUITION BOOK</li><li>ABOUT US</li><li>WEEKLY NEWS</li><li>MY GALLERY</li><li>CONTACT US</li>
  </ul>
</nav>

<section class="abs hero">
  <div class="hero-photo" role="img" aria-label="Photo of Brenna Colfer holding a tin whistle on a coastal cliff"></div>
  <p class="abs hero-text">I am an Irish musician who plays the tin whistle and the flute.</p>
  <div class="abs instrument" style="left:590px;top:214px">Tin<br>Whistle</div>
  <div class="abs instrument" style="left:740px;top:214px">Flute</div>
  <div class="abs slide-arrow" style="left:-16px"><svg width="10" height="12" viewBox="0 0 10 12"><path d="M8 1L2 6l6 5" stroke="#fff" stroke-width="2" fill="none"/></svg></div>
  <div class="abs slide-arrow" style="right:-16px"><svg width="10" height="12" viewBox="0 0 10 12"><path d="M2 1l6 5-6 5" stroke="#fff" stroke-width="2" fill="none"/></svg></div>
</section>
<div class="abs slide-dots"><span></span><span></span><span></span></div>

<main class="abs content-panel">
  <h2 class="abs section-title about-title">About Me</h2>
  <div class="abs about-text">
    <p>Brenna Colfer is considered one of the finest musicians and personalities in the history of Irish music in America. She was born in the Bronx, New York of Irish parents, and she is the second eldest of seven children raised in a musical household. Her mother hails from a small village in County Clare and her father was a well known accordion player from County Galway.</p>
    <a class="btn" style="margin-top:16px">READ MORE</a>
  </div>
  <div class="abs video">
    <div class="video-frame" role="img" aria-label="Video still of the ensemble performing on stage"><span class="video-play"></span></div>
    <div class="video-bar"><i></i></div>
  </div>

  <h2 class="abs section-title title-center" style="top:250px">Tour Dates</h2>
  <article class="abs tour-card" style="left:20px">
    <div class="tour-img" role="img" aria-label="Concert photo with red stage lights" style="background:linear-gradient(135deg,#2a0e0e,#9a2323 55%,#3a1810)"><span class="date-badge">09 FEB 2016</span></div>
    <h3>Lorem ipsum</h3>
    <p>Lorem ipsum dolor sit amet, consectet adipiscing elit. Nulla in sollicitudin.</p>
    <a class="btn">BOOK NOW</a>
  </article>
  <article class="abs tour-card" style="left:315px">
    <div class="tour-img" role="img" aria-label="Ensemble performing in warm stage light" style="background:linear-gradient(135deg,#1e140e,#7a5a3a 55%,#2a1c12)"><span class="date-badge">09 FEB 2016</span></div>
    <h3>Lorem ipsum</h3>
    <p>Lorem ipsum dolor sit amet, consectet adipiscing elit. Nulla in sollicitudin.</p>
    <a class="btn">BOOK NOW</a>
  </article>
  <article class="abs tour-card" style="left:610px">
    <div class="tour-img" role="img" aria-label="Musicians and dancers on a dark stage" style="background:linear-gradient(135deg,#3a2a2a,#8a6a6a 55%,#2a1e1e)"><span class="date-badge">09 FEB 2016</span></div>
    <h3>Lorem ipsum</h3>
    <p>Lorem ipsum dolor sit amet, consectet adipiscing elit. Nulla in sollicitudin.</p>
    <a class="btn">BOOK NOW</a>
  </article>

  <h2 class="abs section-title title-center" style="top:682px">My Gallery</h2>
  <div class="abs gallery" role="img" aria-label="Gallery of performance photographs">
    <div class="feature"><span>Lorem ipsum text dummy text</span></div>
    <div></div><div></div><div></div><div></div>
    <div></div><div></div><div></div><div></div>
  </div>

  <h2 class="abs section-title title-center" style="top:1010px">What Critics Are Saying</h2>
  <blockquote class="abs quote" style="left:20px">"Most distinguished tin whistle & flute player in the world. She has a strong command of every tune she touches, with a warmth of tone and a sure sense of rhythm that few traditional musicians can match."
    <cite>Sean Dorrity <span>— The Harbor Ledger</span></cite></blockquote>
  <blockquote class="abs quote" style="left:470px">"Brenna has become a prominent Irish flute & whistle virtuoso, renowned in Ireland for her musical command and charm. Her long years on the road have made her a true ambassador of the music."
    <cite>Alan Keogh <span>— The Riverside Courier</span></cite></blockquote>
  <div class="abs" style="left:0;top:1270px;width:900px;text-align:center"><a class="btn">VIEW ALL TESTIMONIALS</a></div>
</main>

<footer class="site-footer">
  <div class="abs foot-col" style="left:160px">
    <h4>Quick Links</h4>
    <ul><li>Home</li><li>Meet The Staff</li><li>Tuition Book</li><li>About Us</li><li>Weekly News</li><li>My Gallery</li><li>Contact Us</li></ul>
  </div>
  <div class="abs foot-col" style="left:370px">
    <h4>Quick Enquiry</h4>
    <div class="field"></div><div class="field"></div><div class="field tall"></div>
    <a class="btn" style="background:var(--brown-mid)">Submit</a>
  </div>
  <div class="abs foot-col" style="left:620px">
    <h4>Follow Us</h4>
    <ul class="social"><li><i></i>Friendbook</li><li><i></i>Chirper</li><li><i></i>ViewTube</li><li><i></i>Circles</li></ul>
  </div>
  <div class="abs foot-brand">
    <span class="brand-mark"></span>
    <div class="brand-name">BRENNA COLFER'S<br>MUSICAL TOUR OF IRELAND</div>
  </div>
</footer>
<div class="copyright">Copyright 2016 Brenna Colfer. All Rights Reserved.</div>

</body>
</html>
```